Video App Design

Test of Compatibility
We are looking for a creative designer who is capable of designing mobile application in a trendy manner and at the same time taking into consideration User Interface and technical logic.
This simple test of the design will include 4 different pages, that fits together. In addition, the functions of each page should include the logical buttons required (example Back Button).
1st Page: Design a Video page for Mobile Application.
(Imaging a App which only showcase video shared on Plumtree)
This includes the size size of the video (4:3 and/or 16:9)
The Video should be able to play directly off the page.
The Video layout should include:
1) User Profile Picture and Name
2) Video Name
3) Like Counter/Button
4) Share Button
5) A 160 Character description
6) 5 additional generic icons
7) Rating (Optional)
The toolbar should include the following functions:
1) Change categories
2) Filter
3) Search
4) A Slider Button
2nd Page: Design a Profile Page
It should include:
1) Profile Picture
2) Edit Profile
3) Number of followers
4) Videos that were uploaded by user
5) A button to show videos shared by the User
6) A button to show videos Like by the User
7) An Icon to show verified Account
8) Upload video (Optional: If not, where should this be)
2nd Page Part II - Edit Profile
This will include the fields to be included
1) Real Name
2) Display Name
3) Email Address and change email
4) Password and change password
5) A 160 Character description of the User. (with character count)
2nd Page Part III: Add Video Page
It should include:
1) Choosing categories and subcategories
2) Upload Pictures (Preview of final picture to be uploaded)
3) Upload Video
4) Video Name (preview of final video to be uploaded)
5) Video Description (with character counter)
6) A Huge chunk of words (Example:Terms and Condition)
3rd Page: A Pop up of Video Page
This would include
1) Video
2) Pictures added to the Video
1) User Profile Picture
2) A button to follow the user
3) Video Name
4) Like Counter/Button
5) Share Button
6) A 160 Character description
7) 5 additional generic icons
8) Video Description
9) Rating (Optional)
10) Reviews
11) Displaying the huge chunk of words (Example:Terms and Condition)
You can contact me at info@vemarustudio.com for more information.

```html
<!DOCTYPE html>
<html lang="en">
<head>
<meta charset="utf-8">
<title>Profile – Daniel Hart</title>
<link href="https://fonts.googleapis.com/css2?family=Open+Sans:wght@400;600&display=swap" rel="stylesheet">
<style>
:root{
  --bg:#ffffff;
  --accent:#ee2f6b;
  --text:#4e5d6c;
  --text-dark:#2f3b47;
  --muted:#98a4ae;
  --rule:#d9dde1;
  --stem:#d3d8dc;
  --followers:#45a1dd;
  --videos:#4f6172;
  --shares:#9a78ae;
  --likes:#ee6c5a;
  --verified:#7cbf4f;
  --battery:#5a6b7b;
}
*{margin:0;padding:0;box-sizing:border-box}
html,body{width:676px;height:1200px;overflow:hidden;background:var(--bg)}
body{font-family:"Open Sans",Helvetica,Arial,sans-serif;color:var(--text);position:relative}
.status-bar{position:absolute;top:8px;left:0;width:676px;height:28px;font-size:22px;color:#222}
.status-bar .carrier{position:absolute;left:8px;top:0;display:flex;align-items:center;gap:6px}
.status-bar .time{position:absolute;left:0;width:676px;text-align:center;top:0}
.status-bar .battery{position:absolute;right:8px;top:0;display:flex;align-items:center;gap:8px}
.nav{position:absolute;top:74px;left:0;width:676px;height:40px}
.nav svg{position:absolute}
.avatar{position:absolute;left:238px;top:139px;width:190px;height:190px;border-radius:50%;
  background:radial-gradient(circle at 50% 55%,#c89a80 0%,#a87a63 40%,#6d6258 75%,#9ea4a6 100%)}
.verified-badge{position:absolute;left:375px;top:278px;width:52px;height:52px;border-radius:50%;background:var(--verified);display:flex;align-items:center;justify-content:center}
.profile-name{position:absolute;top:352px;width:676px;text-align:center;font-size:38px;color:var(--text);font-weight:400}
.profile-location{position:absolute;top:410px;width:676px;text-align:center;font-size:23px;color:var(--muted)}
.contact-email{position:absolute;left:36px;top:478px;display:flex;align-items:center;gap:14px;font-size:23px}
.about-title{position:absolute;left:34px;top:542px;font-size:23px;color:var(--text-dark)}
.about-text{position:absolute;left:34px;top:582px;width:620px;font-size:24px;line-height:34px}
.likes-count{position:absolute;left:34px;top:668px;display:flex;align-items:center;gap:8px;font-size:19px}
.more{position:absolute;left:590px;top:677px}
.divider{position:absolute;left:32px;top:730px;width:612px;height:1px;background:var(--rule)}
.stats{position:absolute;left:0;top:740px}
.stat-value{position:absolute;top:1108px;width:120px;text-align:center;color:var(--text)}
.stat-value.primary{font-size:38px;top:1104px}
.stat-value.secondary{font-size:30px;top:1114px}
</style>
</head>
<body>
<div class="status-bar">
  <div class="carrier">
    <svg width="78" height="14" viewBox="0 0 78 14"><g fill="#222"><circle cx="7" cy="7" r="6"/><circle cx="22" cy="7" r="6"/><circle cx="37" cy="7" r="6"/></g><g fill="none" stroke="#222" stroke-width="1.4"><circle cx="52" cy="7" r="5.3"/><circle cx="67" cy="7" r="5.3"/></g></svg>
    <span>Super</span>
    <svg width="22" height="18" viewBox="0 0 22 18"><path d="M11 17 L1 6 A14 14 0 0 1 21 6 Z" fill="#222"/></svg>
  </div>
  <div class="time">11:27AM</div>
  <div class="battery"><span>100%</span>
    <svg width="50" height="22" viewBox="0 0 50 22"><rect x="1" y="2" width="44" height="18" rx="2" fill="none" stroke="#222" stroke-width="1.5"/><rect x="3.5" y="4.5" width="39" height="13" fill="var(--battery)"/><rect x="46" y="8" width="3" height="6" fill="#222"/></svg>
  </div>
</div>

<nav class="nav">
  <svg style="left:32px;top:4px" width="32" height="32" viewBox="0 0 32 32" aria-label="Back"><path d="M30 16H4M15 5 4 16l11 11" fill="none" stroke="var(--accent)" stroke-width="3" stroke-linecap="round" stroke-linejoin="round"/></svg>
  <svg style="left:550px;top:2px" width="36" height="36" viewBox="0 0 36 36" aria-label="Settings"><g fill="var(--accent)"><circle cx="18" cy="18" r="11"/><g id="teeth"><rect x="15" y="2" width="6" height="8" rx="1"/><rect x="15" y="26" width="6" height="8" rx="1"/><rect x="2" y="15" width="8" height="6" rx="1"/><rect x="26" y="15" width="8" height="6" rx="1"/></g><use href="#teeth" transform="rotate(45 18 18)"/></g><circle cx="18" cy="18" r="5" fill="#fff"/></svg>
  <svg style="left:616px;top:4px" width="30" height="30" viewBox="0 0 30 30" aria-label="Add"><path d="M15 3v24M3 15h24" stroke="var(--accent)" stroke-width="3" stroke-linecap="round"/></svg>
</nav>

<div class="avatar" role="img" aria-label="Profile photo of Daniel Hart"></div>
<div class="verified-badge" aria-label="Verified account"><svg width="20" height="16" viewBox="0 0 20 16"><path d="M3 8l5 5 9-10" fill="none" stroke="#fff" stroke-width="2.6" stroke-linecap="round" stroke-linejoin="round"/></svg></div>

<h1 class="profile-name">Daniel Hart</h1>
<div class="profile-location">Singapore</div>

<div class="contact-email">
  <svg width="24" height="18" viewBox="0 0 24 18"><rect x="0" y="1" width="24" height="16" rx="1.5" fill="#222"/><path d="M1 2l11 8 11-8" fill="none" stroke="#fff" stroke-width="1.6"/></svg>
  <span>daniel.hart@inboxmail.com</span>
</div>

<h2 class="about-title" style="font-weight:400">About Daniel</h2>
<p class="about-text">Artist. Designer. Coffee lover. I live in Singapore, and I love it!</p>

<div class="likes-count">
  <svg width="20" height="18" viewBox="0 0 20 18"><path d="M10 17S1 11 1 5.5A4.5 4.5 0 0 1 10 3.5 4.5 4.5 0 0 1 19 5.5C19 11 10 17 10 17Z" fill="var(--likes)"/></svg>
  <span>1,203 likes</span>
</div>
<svg class="more" width="44" height="10" viewBox="0 0 44 10" aria-label="More"><g fill="#333"><circle cx="5" cy="5" r="4.5"/><circle cx="22" cy="5" r="4.5"/><circle cx="39" cy="5" r="4.5"/></g></svg>

<div class="divider"></div>

<svg class="stats" width="676" height="360" viewBox="0 740 676 360">
  <line x1="79" y1="1077" x2="606" y2="1077" stroke="var(--stem)" stroke-width="1.2"/>
  <line x1="79" y1="900" x2="79" y2="1077" stroke="var(--followers)" stroke-width="1.2"/>
  <line x1="264" y1="940" x2="264" y2="1077" stroke="var(--stem)" stroke-width="1.2"/>
  <line x1="432" y1="880" x2="432" y2="1077" stroke="var(--stem)" stroke-width="1.2"/>
  <line x1="605" y1="820" x2="605" y2="1077" stroke="var(--stem)" stroke-width="1.2"/>
  <circle cx="79" cy="1077" r="5" fill="var(--followers)"/>

  <g aria-label="Followers">
    <circle cx="79" cy="879" r="53" fill="var(--followers)"/>
    <g fill="#fff">
      <circle cx="79" cy="864" r="6"/><rect x="72" y="871" width="14" height="24" rx="3"/>
      <circle cx="66" cy="867" r="4.5"/><rect x="60" y="873" width="10" height="17" rx="2.5"/>
      <circle cx="92" cy="867" r="4.5"/><rect x="88" y="873" width="10" height="17" rx="2.5"/>
    </g>
  </g>
  <g aria-label="Videos">
    <circle cx="264" cy="926" r="37" fill="var(--videos)"/>
    <rect x="251" y="912" width="26" height="28" rx="2" fill="#fff"/>
    <g fill="var(--videos)">
      <rect x="258" y="916" width="12" height="9"/><rect x="258" y="928" width="12" height="9"/>
      <rect x="253" y="915" width="3" height="3"/><rect x="253" y="921" width="3" height="3"/><rect x="253" y="927" width="3" height="3"/><rect x="253" y="933" width="3" height="3"/>
      <rect x="272" y="915" width="3" height="3"/><rect x="272" y="921" width="3" height="3"/><rect x="272" y="927" width="3" height="3"/><rect x="272" y="933" width="3" height="3"/>
    </g>
  </g>
  <g aria-label="Shares">
    <circle cx="432" cy="863" r="37" fill="var(--shares)"/>
    <path d="M420 858v16h22v-7" fill="none" stroke="#fff" stroke-width="2.6"/>
    <path d="M425 866c2-7 7-10 14-10v-5l8 7-8 7v-5c-6 0-10 2-14 6Z" fill="#fff"/>
  </g>
  <g aria-label="Likes">
    <circle cx="605" cy="799" r="37" fill="var(--likes)"/>
    <path d="M605 811s-12-7-12-15a6 6 0 0 1 12-2 6 6 0 0 1 12 2c0 8-12 15-12 15Z" fill="#fff"/>
  </g>
</svg>

<div class="stat-value primary" style="left:19px">637</div>
<div class="stat-value secondary" style="left:204px">38</div>
<div class="stat-value secondary" style="left:372px">2k</div>
<div class="stat-value secondary" style="left:545px">3k</div>
</body>
</html>
```